COMMERCIAL DOOR REPAIR
BUSINESS CARDS, LETTERHEAD, ENVELOPES, FAX COVER, EMAIL SIGNATURE
Rob Whitfield
NFPEI Certified Door Inspector
1752 E Pinnell Ln Cactus Flats, AZ 85317
service@robsgatefix.com
www.robsgatefix.com
ROC# 514037
Not sure if font in logo can be used - open to other fonts as well. just no script or femine fonts. Not sure if all items on back will fit - open to re-wording, suggestions, etc.
24 Hour Emergency Services Available Specializing in: Automatic Doors Manual Doors Vitrelon Glass Doors Hollow Metal Doors Revolving Doors Also specializing in: Glass Mirrors Locksmithing Shower Doors Roof Hatches Re-seals Board-Ups

```html
<!DOCTYPE html>
<html lang="en">
<head>
<meta charset="utf-8">
<title>Whitfield Entry Service – Stationery Set</title>
<link href="https://fonts.googleapis.com/css2?family=Roboto:wght@400;700&display=swap" rel="stylesheet">
<style>
:root{
  --brand-blue:#1677cf;
  --brand-blue-light:#7cc2f2;
  --brand-navy:#1d3f73;
  --accent-red:#c8102e;
  --ink:#333;
  --muted:#777;
  --paper:#fff;
  --bg:#fff;
}
*{box-sizing:border-box;margin:0;padding:0}
html,body{width:1200px;height:506px;overflow:hidden;background:var(--bg);font-family:"Roboto",Arial,sans-serif;color:var(--ink)}
.canvas{position:relative;width:1200px;height:506px}

.sheet{position:absolute;background:var(--paper);box-shadow:0 1px 4px rgba(0,0,0,.25);overflow:hidden}
.fax{left:29px;top:18px;width:350px;height:470px}
.letterhead{left:396px;top:18px;width:348px;height:470px}

.header-band{position:absolute;left:0;right:0;top:10px;height:30px;background:linear-gradient(90deg,#fff 0%,#d9ecfb 35%,var(--brand-blue-light) 65%,var(--brand-blue) 100%)}
.brand{position:absolute;display:flex;align-items:center;gap:6px}
.brand-mark{width:26px;height:26px;background:var(--brand-blue);border:2px solid #fff;box-shadow:0 0 0 1px var(--brand-blue);flex:none}
.brand-name{font-weight:400;color:var(--brand-navy);font-size:13px;white-space:nowrap}
.sheet .brand{left:10px;top:12px}
.tagline{position:absolute;left:44px;top:42px;font-size:5px;color:var(--muted);letter-spacing:.4px}

.fax-fields{position:absolute;left:22px;top:88px;width:300px;display:grid;grid-template-columns:1fr 1fr;row-gap:10px;column-gap:26px}
.field{display:flex;align-items:flex-end;gap:4px;font-size:6px;font-weight:700}
.field span{width:26px}
.field i{flex:1;border-bottom:.6px solid #999;height:7px}
.fax-options{position:absolute;left:22px;top:150px;display:flex;gap:16px;font-size:5.5px}
.fax-options label{display:flex;align-items:center;gap:3px}
.fax-options b{width:6px;height:6px;border:.6px solid #666;display:inline-block}

.footer{position:absolute;left:16px;bottom:16px;font-size:5px;line-height:7.5px;color:var(--ink)}
.footer a{color:var(--accent-red);text-decoration:none}
.footer-rule{position:absolute;left:0;right:0;bottom:8px;height:3px;background:var(--brand-blue)}
.footer-rule::after{content:"";position:absolute;left:0;right:0;top:3px;height:2px;background:var(--accent-red)}

.card{position:absolute;box-shadow:0 1px 4px rgba(0,0,0,.3);overflow:hidden}
.card-front{left:809px;top:108px;width:194px;height:84px;background:var(--paper)}
.card-front .brand{left:7px;top:6px;gap:5px}
.card-front .brand-mark{width:16px;height:16px}
.card-front .brand-name{font-size:8px}
.card-person{position:absolute;right:8px;top:26px;text-align:right;font-size:6px;color:var(--accent-red);font-weight:700;line-height:8px}
.card-person small{display:block;color:var(--muted);font-weight:400;font-size:4.5px}
.card-contact{position:absolute;left:8px;top:44px;font-size:4.3px;line-height:6.2px}
.card-front .bar{position:absolute;left:0;right:0;bottom:0;height:6px;background:var(--brand-blue)}
.card-front .bar::before{content:"";position:absolute;left:0;right:0;top:-2px;height:2px;background:var(--accent-red)}

.card-back{left:912px;top:226px;width:144px;height:74px;background:linear-gradient(135deg,var(--brand-blue) 0%,#3a9be3 60%,var(--brand-blue-light) 100%);color:#fff}
.card-back .services{position:absolute;left:7px;top:8px;font-size:3.8px;line-height:5.6px}
.card-back .services strong{font-size:4.6px}
.card-back .brand{right:6px;bottom:5px;gap:3px}
.card-back .brand-mark{width:8px;height:8px;border-width:1px}
.card-back .brand-name{font-size:5px;color:#fff}

.envelope{position:absolute;left:775px;top:319px;width:394px;height:168px;background:var(--paper);box-shadow:0 1px 4px rgba(0,0,0,.3);overflow:hidden}
.envelope .wash{position:absolute;left:0;right:0;top:0;height:84px;background:linear-gradient(180deg,var(--brand-blue) 0%,#4aa6e8 55%,#fff 100%)}
.envelope .brand-mark{position:absolute;left:180px;top:14px;width:34px;height:34px}
.envelope .brand-name{position:absolute;left:0;right:0;top:52px;text-align:center;font-size:6px;color:#fff}
.envelope .return{position:absolute;left:14px;top:92px;font-size:5px;line-height:7px}
.envelope .rule{position:absolute;left:0;right:0;bottom:6px;height:2px;background:var(--accent-red)}
</style>
</head>
<body>
<div class="canvas">

  <section class="sheet fax" aria-label="Fax cover sheet">
    <div class="header-band"></div>
    <div class="brand"><div class="brand-mark"></div><div class="brand-name">Whitfield Entry Service</div></div>
    <div class="tagline">COMMERCIAL DOOR REPAIR</div>
    <div class="fax-fields">
      <div class="field"><span>To:</span><i></i></div>
      <div class="field"><span>From:</span><i></i></div>
      <div class="field"><span>Fax:</span><i></i></div>
      <div class="field"><span>Pages:</span><i></i></div>
      <div class="field"><span>Phone:</span><i></i></div>
      <div class="field"><span>Date:</span><i></i></div>
      <div class="field"><span>Re:</span><i></i></div>
      <div class="field"><span>CC:</span><i></i></div>
    </div>
    <div class="fax-options">
      <label><b></b>Urgent</label>
      <label><b></b>For Review</label>
      <label><b></b>Please Comment</label>
      <label><b></b>Please Reply</label>
      <label><b></b>Please Recycle</label>
    </div>
    <div class="footer">
      1752 E Pinnell Ln Cactus Flats, AZ 85317<br>
      Toll Free: 877-555-0142 Phone: 623-555-0188 Fax: 623-555-0190<br>
      Email: service@robsgatefix.com | <a>www.robsgatefix.com</a><br>
      ROC# 514037
    </div>
    <div class="footer-rule"></div>
  </section>

  <section class="sheet letterhead" aria-label="Letterhead">
    <div class="header-band"></div>
    <div class="brand"><div class="brand-mark"></div><div class="brand-name">Whitfield Entry Service</div></div>
    <div class="tagline">COMMERCIAL DOOR REPAIR</div>
    <div class="footer">
      1752 E Pinnell Ln Cactus Flats, AZ 85317<br>
      Toll Free: 877-555-0142 Phone: 623-555-0188 Fax: 623-555-0190<br>
      Email: service@robsgatefix.com | <a>www.robsgatefix.com</a>
    </div>
    <div class="footer-rule"></div>
  </section>

  <section class="card card-front" aria-label="Business card front">
    <div class="brand"><div class="brand-mark"></div><div class="brand-name">Whitfield Entry Service</div></div>
    <div class="card-person">Rob Whitfield<small>NFPEI Certified Door Inspector</small></div>
    <div class="card-contact">
      1752 E Pinnell Ln Cactus Flats, AZ 85317<br>
      Phone: 623-555-0188 Fax: 623-555-0190<br>
      service@robsgatefix.com<br>
      www.robsgatefix.com &nbsp; ROC# 514037
    </div>
    <div class="bar"></div>
  </section>

  <section class="card card-back" aria-label="Business card back">
    <div class="services">
      <strong>24 Hour Emergency Services Available</strong><br>
      Specializing in: Automatic, Manual, Vitrelon Glass,<br>
      Hollow Metal &amp; Revolving Doors<br>
      Also: Glass Mirrors, Locksmithing, Shower Doors,<br>
      Roof Hatches, Re-seals, Board-Ups
    </div>
    <div class="brand"><div class="brand-mark"></div><div class="brand-name">Whitfield Entry Service</div></div>
  </section>

  <section class="envelope" aria-label="Envelope">
    <div class="wash"></div>
    <div class="brand-mark"></div>
    <div class="brand-name">Whitfield Entry Service</div>
    <div class="return">1752 E Pinnell Ln Cactus Flats, AZ 85317</div>
    <div class="rule"></div>
  </section>

</div>
</body>
</html>
```